Top 100

I have attached a sheet with the information that we would like on a 2'by 3' poster. If you can take this info and make it look more appealing, that is what we are looking for.

I have also attached our high res logo. We just pulled the KVRT and Trelvex logos off the web

```html
<!DOCTYPE html>
<html lang="en">
<head>
<meta charset="utf-8">
<title>Veritan Advisors – Recognition Poster</title>
<link href="https://fonts.googleapis.com/css2?family=Roboto+Condensed:wght@400;700&display=swap" rel="stylesheet">
<style>
  :root {
    --navy: #173a62;
    --orange: #f7941d;
    --white: #ffffff;
    --slate: #3b5673;
    --grey: #7d8a92;
    --page: #ffffff;
  }
  * { margin: 0; padding: 0; box-sizing: border-box; }
  html, body { width: 1200px; height: 1000px; overflow: hidden; background: var(--page); }
  body { position: relative; font-family: "Roboto Condensed", "Arial Narrow", sans-serif; }

  .poster { position: absolute; left: 283px; top: 30px; width: 627px; height: 938px; background: var(--white); }

  .masthead { height: 158px; display: flex; flex-direction: column; align-items: center; justify-content: center; padding-top: 8px; }
  .brand { display: flex; align-items: center; gap: 16px; }
  .brand-mark { width: 30px; height: 30px; background: var(--grey); }
  .brand-name { color: var(--slate); font-weight: 700; font-size: 58px; line-height: 1; letter-spacing: 0.5px; }
  .brand-sub { color: var(--slate); font-weight: 700; font-size: 13px; letter-spacing: 1px; margin-left: 100px; margin-top: 4px; }

  .hero { height: 118px; display: flex; }
  .hero-columns { flex: 0 0 376px; background: linear-gradient(90deg, #6f6f6f 0%, #b9b9b9 25%, #8d8d8d 50%, #c9c9c9 75%, #9a9a9a 100%); }
  .hero-glass { flex: 1; background: linear-gradient(135deg, #4f86b5 0%, #a6cbe6 45%, #e4f1fa 100%); }

  .band-top { height: 30px; background: var(--orange); }
  .field { height: 612px; background: var(--navy); position: relative; }
  .band-bottom { height: 20px; background: var(--orange); }

  .row { position: absolute; left: 36px; width: 552px; height: 169px; display: flex; align-items: center; }
  .row:nth-child(1) { top: 29px; }
  .row:nth-child(2) { top: 218px; }
  .row:nth-child(3) { top: 407px; }

  .badge { width: 170px; height: 169px; background: var(--white); display: flex; align-items: center; justify-content: center; }
  .badge-name { font-weight: 700; font-size: 30px; color: var(--slate); }

  .connector { width: 26px; height: 2px; background: var(--white); }

  .claim { width: 356px; height: 169px; border: 2px solid var(--white); display: flex; flex-direction: column; align-items: center; justify-content: center; text-align: center; color: var(--white); font-size: 24px; line-height: 1.38; }
  .claim .accent { color: var(--orange); font-weight: 700; font-size: 27px; line-height: 1.25; }
</style>
</head>
<body>
  <div class="poster">
    <header class="masthead">
      <div class="brand">
        <span class="brand-mark"></span>
        <span class="brand-name">Veritan</span>
      </div>
      <div class="brand-sub">ADVISORS</div>
    </header>

    <div class="hero">
      <div class="hero-columns" role="img" aria-label="Photo of classical stone columns on a grand building facade"></div>
      <div class="hero-glass" role="img" aria-label="Photo looking up at a modern glass skyscraper"></div>
    </div>

    <div class="band-top"></div>

    <section class="field">
      <div class="row">
        <div class="badge"><span class="badge-name">KVRT</span></div>
        <div class="connector"></div>
        <div class="claim">
          <span class="accent">2015 - Top 100</span>
          <span class="accent">Wealth Management Firm</span>
          <span>Only Greater Cincinnati</span>
          <span>Firm Selected</span>
        </div>
      </div>

      <div class="row">
        <div class="badge"><span class="badge-name">Trelvex</span></div>
        <div class="connector"></div>
        <div class="claim">
          <span>In 2015 Launches the</span>
          <span class="accent">Nation’s Only Actively</span>
          <span class="accent">ManagedSmall Cap ETF</span>
          <span>(QSCP: TRELVEX)</span>
        </div>
      </div>

      <div class="row">
        <div class="badge"><span class="badge-name">Veritan</span></div>
        <div class="connector"></div>
        <div class="claim">
          <span>Nationally Recognised Advisor</span>
          <span class="accent">Providing Boutique Wealth</span>
          <span class="accent">Management Since 1999</span>
        </div>
      </div>
    </section>

    <div class="band-bottom"></div>
  </div>
</body>
</html>
```